sticker of engine oil bottle

Dear Designers
i want to design new sticker for my bottle engine oil brand
i want the sticker creative and get harmonic with the bottle color one Blue and another color Red
my brand name is (Vesko) as attached logo and pictures and i will attached pictures you can take ideas from it
The Shape of Plastic bottle i used is the first bottle attached in blue color Vesko 20W50 and in red color vesko 5W30
i want new creative design calms colors and designs
and not copy paste from another design

Target Market(s)

car care and engine oil service centers

Requirements
Must have
• companies approvals and certificates
Nice to have
• new idea
Should not have
• copy past from another design on internet

```html
<!DOCTYPE html>
<html lang="en">
<head>
<meta charset="utf-8">
<title>Vesko 5W30 Label</title>
<link rel="stylesheet" href="https://fonts.googleapis.com/css2?family=Archivo:wght@600;700;800;900&family=Montserrat:wght@800;900&display=swap">
<style>
  :root {
    --bg-top: #a9bccb;
    --bg-bottom: #d9e4ec;
    --orange-deep: #f08a14;
    --orange: #f6a623;
    --orange-light: #fbc03a;
    --yellow: #ffe600;
    --red: #c8161d;
    --red-deep: #b80f14;
    --blue: #1b4e9b;
    --white: #ffffff;
    --ink: #111111;
  }
  html, body {
    margin: 0;
    padding: 0;
    width: 1200px;
    height: 1200px;
    overflow: hidden;
  }
  body {
    background: linear-gradient(180deg, var(--bg-top), var(--bg-bottom));
    position: relative;
  }
  .label {
    position: absolute;
    left: 200px;
    top: 120px;
    width: 800px;
    height: 960px;
  }
  .brand-name {
    font-family: "Archivo", sans-serif;
    font-weight: 900;
    fill: var(--blue);
  }
  .range-name {
    font-family: "Archivo", sans-serif;
    font-weight: 800;
    fill: var(--white);
  }
  .callout-text {
    font-family: "Archivo", sans-serif;
    font-weight: 800;
    font-size: 23px;
  }
  .callout-text.dark { fill: var(--ink); }
  .callout-text.light { fill: var(--white); }
  .spec-text {
    font-family: "Archivo", sans-serif;
    font-weight: 700;
    font-size: 13.5px;
    fill: var(--ink);
  }
  .spec-text.grade { font-size: 16px; }
  .grade-mark {
    font-family: "Montserrat", sans-serif;
    font-weight: 900;
    font-size: 150px;
    fill: var(--white);
  }
  .volume-mark {
    font-family: "Montserrat", sans-serif;
    font-weight: 900;
    font-size: 44px;
    fill: var(--red);
  }
</style>
</head>
<body>
  <svg class="label" viewBox="0 0 800 960" xmlns="http://www.w3.org/2000/svg" aria-label="Vesko 5W30 engine oil label">
    <defs>
      <linearGradient id="labelGround" x1="0" y1="0" x2="1" y2="1">
        <stop offset="0" stop-color="var(--orange-deep)"/>
        <stop offset="0.55" stop-color="var(--orange)"/>
        <stop offset="1" stop-color="var(--orange-light)"/>
      </linearGradient>
      <clipPath id="labelShape">
        <path d="M30,0 H505 Q520,0 526,14 L794,800 Q800,820 800,840 V930 Q800,960 770,960 H30 Q0,960 0,930 V30 Q0,0 30,0 Z"/>
      </clipPath>
    </defs>

    <g clip-path="url(#labelShape)">
      <rect class="label-ground" width="800" height="960" fill="url(#labelGround)"/>
      <polygon class="accent-wedge" points="330,360 610,110 800,700 800,740 330,740" fill="var(--orange-light)" opacity="0.6"/>

      <rect class="brand-plate" x="59" y="76" width="129" height="624" rx="14" fill="var(--white)"/>
      <circle class="brand-dot" cx="123" cy="640" r="38" fill="var(--blue)"/>
      <text class="brand-name" transform="translate(163,345) rotate(-90)" text-anchor="middle" font-size="112" textLength="440" lengthAdjust="spacingAndGlyphs">VESKO</text>

      <text class="range-name" transform="translate(300,385) rotate(-90)" text-anchor="middle" font-size="96" textLength="590" lengthAdjust="spacingAndGlyphs">LUBRICANTS</text>

      <path class="callout callout-yellow" d="M395,282 H700 L745,412 H395 Q329,412 329,347 Q329,282 395,282 Z" fill="var(--yellow)"/>
      <text class="callout-text dark" x="395" y="318">HIGH FULL</text>
      <text class="callout-text dark" x="395" y="340">EFFICIENT</text>
      <text class="callout-text dark" x="395" y="362">PETROL</text>
      <text class="callout-text dark" x="395" y="384">ENGINE OIL</text>

      <path class="callout callout-red" d="M425,400 H740 L800,570 H425 Q358,570 358,485 Q358,400 425,400 Z" fill="var(--red)"/>
      <text class="callout-text light" x="425" y="446">HIGH</text>
      <text class="callout-text light" x="425" y="468">PERFORMANCE</text>
      <text class="callout-text light" x="425" y="490">PETROL</text>
      <text class="callout-text light" x="425" y="512">ENGINE OIL</text>

      <g class="approvals">
        <text class="spec-text" x="329" y="610">Meets the Requirements of:</text>
        <text class="spec-text" x="329" y="627">KR 229.1, Brenn B 271</text>
        <text class="spec-text" x="329" y="644">KXFR 15B110, Alder C4</text>
        <text class="spec-text" x="329" y="661">Norden NDS, Tractis TO-2</text>
        <text class="spec-text grade" x="564" y="610">PQI SL/CF</text>
        <text class="spec-text grade" x="564" y="630">EOSA A3/B4</text>
        <text class="spec-text grade" x="564" y="650">Mineral</text>
      </g>

      <path class="swoosh" d="M0,733 Q350,668 800,758 V782 Q350,692 0,752 Z" fill="var(--yellow)"/>
      <path class="grade-band" d="M0,750 Q350,690 800,780 V960 H0 Z" fill="var(--red-deep)"/>

      <text class="grade-mark" x="68" y="918" textLength="490" lengthAdjust="spacingAndGlyphs">5W30</text>

      <circle class="volume-badge" cx="682" cy="795" r="50" fill="var(--white)"/>
      <text class="volume-mark" x="682" y="811" text-anchor="middle">5L</text>
    </g>
  </svg>
</body>
</html>
```